Ridgeline Yard Works Stationary Package
Business Cards, Letterhead, Envelope, Sticker, Fax Cover sheet, invoice, and estimate
Ridgeline Yard Works Stationary Package - Construction
Creative Brief
Use same font as used in my logo
Pete Marrow
Owner
4172 W. Fenwick Rd. Burbank, IL 60421
petemarrow@quailnet.example
www.ridgelineyardworks.example
Can information be in a format that can be edited for future use. ex: Name Changes, New Numbers, etc?

```html
<!DOCTYPE html>
<html lang="en">
<head>
<meta charset="utf-8">
<title>Ridgeline Yard Works — Business Card</title>
<link rel="stylesheet" href="https://fonts.googleapis.com/css2?family=Arimo:wght@400;700&family=Exo+2:wght@600&display=swap">
<style>
  :root {
    --backdrop: #e9e6e1;
    --card: #ffffff;
    --ink: #1c1c1c;
    --ink-soft: #333333;
    --rule: #c9c9c9;
    --accent: #c8202a;
    --brand: #1f6fb8;
  }
  * { margin: 0; padding: 0; box-sizing: border-box; }
  html, body {
    width: 1200px;
    height: 778px;
    overflow: hidden;
    background: var(--backdrop);
  }
  .canvas {
    position: relative;
    width: 1200px;
    height: 778px;
  }
  .business-card {
    position: absolute;
    left: 160px;
    top: 139px;
    width: 880px;
    height: 500px;
    background: var(--card);
    border-radius: 30px;
    box-shadow: 0 6px 18px rgba(0,0,0,0.18);
    font-family: "Arimo", Arial, sans-serif;
    color: var(--ink);
  }
  .brand {
    position: absolute;
    left: 120px;
    top: 74px;
    display: flex;
    align-items: center;
    gap: 24px;
  }
  .brand-mark {
    width: 96px;
    height: 96px;
    background: var(--brand);
    border-radius: 8px;
    flex: none;
  }
  .brand-text { display: flex; flex-direction: column; align-items: center; }
  .brand-name {
    font-family: "Exo 2", "Arimo", sans-serif;
    font-weight: 600;
    font-size: 47px;
    line-height: 1;
    color: var(--ink);
    white-space: nowrap;
  }
  .brand-tagline {
    display: flex;
    align-items: center;
    gap: 14px;
    margin-top: 10px;
    font-size: 25px;
    color: var(--ink-soft);
    white-space: nowrap;
  }
  .brand-tagline::before,
  .brand-tagline::after {
    content: "";
    width: 56px;
    height: 2px;
    background: var(--ink);
  }
  .divider {
    position: absolute;
    left: 432px;
    top: 240px;
    width: 2px;
    height: 220px;
    background: linear-gradient(to bottom, rgba(201,201,201,0), var(--rule) 20%, var(--rule) 80%, rgba(201,201,201,0));
  }
  .person {
    position: absolute;
    right: 515px;
    top: 300px;
    text-align: right;
  }
  .person-name { font-size: 31px; font-weight: 700; line-height: 1.1; }
  .person-role { font-size: 21px; font-weight: 700; color: var(--ink-soft); margin-top: 4px; }
  .contact {
    position: absolute;
    left: 497px;
    top: 246px;
    font-size: 21px;
    line-height: 1.35;
    color: var(--ink-soft);
  }
  .address { margin-bottom: 14px; }
  .contact-list { list-style: none; }
  .contact-list li { display: flex; align-items: center; gap: 10px; }
  .contact-icon { width: 16px; height: 16px; fill: var(--accent); flex: none; }
</style>
</head>
<body>
<main class="canvas">
  <section class="business-card">
    <div class="brand">
      <div class="brand-mark"></div>
      <div class="brand-text">
        <div class="brand-name">Ridgeline Yard Works</div>
        <div class="brand-tagline">Home Restoration Specialists</div>
      </div>
    </div>

    <div class="divider"></div>

    <div class="person">
      <div class="person-name">Pete Marrow</div>
      <div class="person-role">Owner</div>
    </div>

    <div class="contact">
      <p class="address">4172 W. Fenwick Rd.<br>Burbank, IL 60421</p>
      <ul class="contact-list">
        <li>
          <svg class="contact-icon" viewBox="0 0 16 16" aria-hidden="true"><rect x="4" y="0" width="8" height="16" rx="2"/><rect x="5.5" y="2" width="5" height="7" fill="#fff"/></svg>
          (708) 555-0142
        </li>
        <li>
          <svg class="contact-icon" viewBox="0 0 16 16" aria-hidden="true"><rect x="4" y="0" width="8" height="5"/><rect x="0" y="5" width="16" height="8" rx="1.5"/><rect x="4" y="10" width="8" height="6" fill="#fff" stroke="#c8202a" stroke-width="1.5"/></svg>
          (708) 555-0178
        </li>
        <li>
          <svg class="contact-icon" viewBox="0 0 16 16" aria-hidden="true"><rect x="0" y="3" width="16" height="11" rx="1"/><path d="M1 4 L8 9.5 L15 4" fill="none" stroke="#fff" stroke-width="1.5"/></svg>
          petemarrow@quailnet.example
        </li>
        <li>
          <svg class="contact-icon" viewBox="0 0 16 16" aria-hidden="true"><circle cx="8" cy="8" r="8"/><path d="M0.5 8 H15.5 M8 0.5 C4 4 4 12 8 15.5 M8 0.5 C12 4 12 12 8 15.5" fill="none" stroke="#fff" stroke-width="1.2"/></svg>
          www.ridgelineyardworks.example
        </li>
      </ul>
    </div>
  </section>
</main>
</body>
</html>
```